LETTERHEAD & ENVELOPE: eye-catching stationary design for our custom office furniture business

Our company recently rebranded and we are in need of new stationary. Specifically, we need branded letterhead for standard paper size (8.5” x 11”), and matching envelopes, size: #9.

All designs should incorporate our brand colors, brand typeface, and logo. Please view attached brand guidelines document for brand colors, and brand description.

Letterhead: 8.5” x 11” Must include CoralvexKTN Logo, Dorrit Falke Certified Dealer Logo, mailing address, phone number, website, and email address.

Envelope: 9.5” x 4.125” Must include CoralvexKTN Logo, mailing address, and Dorrit Falke Certified Dealer Logo.

Attached files include:

```html
<!DOCTYPE html>
<html lang="en">
<head>
<meta charset="utf-8">
<title>CoralvexKTN Stationery</title>
<link href="https://fonts.googleapis.com/css2?family=Montserrat:wght@300;400&family=Lato:wght@400;700&display=swap" rel="stylesheet">
<style>
  :root {
    --brand-green: #557a6a;
    --brand-grey: #4a4a4c;
    --paper: #f5f5f4;
    --backdrop: #e2e2e2;
    --ink: #2b2b2b;
    --white: #ffffff;
    --signature-tone: #dcdcdc;
  }
  * { box-sizing: border-box; margin: 0; padding: 0; }
  html, body { width: 798px; height: 1200px; overflow: hidden; }
  body {
    background: var(--backdrop);
    font-family: "Lato", sans-serif;
    color: var(--ink);
    position: relative;
  }
  .sheet {
    position: absolute;
    background: var(--paper);
    box-shadow: 0 2px 8px rgba(0,0,0,0.12);
    overflow: hidden;
  }
  .bands { position: absolute; inset: 0; width: 100%; height: 100%; }
  .brand {
    position: absolute;
    display: flex;
    align-items: center;
    gap: 8px;
  }
  .brand-mark {
    border-radius: 50%;
    background: var(--brand-green);
  }
  .brand-name {
    font-family: "Montserrat", sans-serif;
    font-weight: 300;
    color: var(--brand-green);
    letter-spacing: 0.5px;
  }
  .dealer {
    position: absolute;
    display: flex;
    align-items: center;
    gap: 5px;
    font-family: "Lato", sans-serif;
    font-weight: 400;
    color: var(--ink);
    white-space: nowrap;
  }
  .dealer-mark { border-radius: 50%; background: #1e1e1e; flex: none; }
  .website {
    position: absolute;
    color: var(--white);
    font-family: "Lato", sans-serif;
    white-space: nowrap;
  }

  /* Letterhead */
  .letterhead { left: 179px; top: 30px; width: 440px; height: 569px; }
  .letterhead .brand { left: 36px; top: 62px; }
  .letterhead .brand-mark { width: 30px; height: 30px; }
  .letterhead .brand-name { font-size: 24px; }
  .letter-body {
    position: absolute;
    left: 60px; top: 128px; width: 330px;
    font-size: 7.6px; line-height: 10.5px;
  }
  .letter-body p { margin-bottom: 9px; }
  .letter-body .date, .letter-body .recipient { margin-bottom: 8px; }
  .letter-body .salutation { font-weight: 700; font-size: 9.5px; margin-bottom: 7px; }
  .letter-body .closing { margin-top: 12px; margin-left: 110px; margin-bottom: 6px; }
  .signature {
    margin-left: 110px;
    width: 120px; height: 28px;
    background: var(--signature-tone);
    border-radius: 3px;
  }
  .footer-address {
    position: absolute; left: 128px; top: 513px;
    color: var(--white); font-size: 7.5px; line-height: 11px;
    white-space: nowrap;
  }
  .footer-divider {
    position: absolute; left: 240px; top: 513px;
    width: 1px; height: 22px; background: var(--white);
  }
  .footer-contact {
    position: absolute; left: 247px; top: 512px;
    color: var(--white); font-size: 7.5px; line-height: 12px;
    white-space: nowrap;
  }
  .footer-contact span { display: flex; align-items: center; gap: 4px; }
  .footer-contact svg { width: 7px; height: 7px; flex: none; }
  .letterhead .dealer { left: 318px; top: 474px; font-size: 6.5px; }
  .letterhead .dealer-mark { width: 12px; height: 12px; }
  .letterhead .website { left: 368px; top: 498px; font-size: 7px; }

  /* Envelopes */
  .envelope-front { left: 149px; top: 630px; width: 500px; height: 217px; }
  .envelope-front .brand { left: 22px; top: 22px; }
  .envelope-front .brand-mark { width: 26px; height: 26px; }
  .envelope-front .brand-name { font-size: 22px; }
  .envelope-address {
    position: absolute; left: 16px; top: 150px;
    color: var(--white); font-size: 8.5px; white-space: nowrap;
  }
  .envelope-front .dealer { left: 300px; top: 168px; font-size: 8px; color: var(--white); }
  .envelope-front .dealer-mark { width: 14px; height: 14px; background: var(--white); }
  .envelope-front .website { left: 300px; top: 190px; font-size: 8px; }
  .envelope-back { left: 149px; top: 880px; width: 500px; height: 217px; }
</style>
</head>
<body>

<section class="sheet letterhead" aria-label="Letterhead">
  <svg class="bands" viewBox="0 0 440 569" aria-hidden="true">
    <polygon points="0,0 262,0 256,12 0,12" fill="var(--brand-grey)"/>
    <polygon points="262,0 440,0 440,20 250,20" fill="var(--brand-green)"/>
    <polygon points="120,505 340,505 358,545 120,545" fill="var(--brand-green)"/>
    <polygon points="350,488 440,488 440,516 363,516" fill="var(--brand-grey)"/>
  </svg>

  <div class="brand">
    <span class="brand-mark"></span>
    <span class="brand-name">CoralvexKTN</span>
  </div>

  <div class="letter-body">
    <p class="date">Jun-03-2021</p>
    <p class="recipient">Mr. John Doe<br>President</p>
    <p class="recipient">Link Corporation<br>123 Street Name, Suite# 10<br>City, State, 120023</p>
    <p class="salutation">Dear Mr. John</p>
    <p>Lorem ipsum dolor sit amet, consectetur adipisicing elit, sed do eiusmod tempor incididunt ut labore et dolore magna aliqua. Ut enim ad minim veniam, quis nostrud exercitation ullamco laboris nisi ut aliquip ex ea commodo consequat. Duis aute irure dolor in reprehenderit in voluptate velit esse cillum dolore eu fugiat nulla pariatur.</p>
    <p>Lorem ipsum dolor sit amet, consectetur adipisicing elit, sed do eiusmod tempor incididunt ut labore et dolore magna aliqua. Ut enim ad minim veniam, quis nostrud exercitation ullamco laboris nisi ut aliquip ex ea commodo consequat. Duis aute irure dolor in reprehenderit in voluptate velit esse cillum dolore eu fugiat nulla pariatur.</p>
    <p>Lorem ipsum dolor sit amet, consectetur adipisicing elit, sed do eiusmod tempor incididunt ut labore et dolore magna aliqua. Ut enim ad minim veniam, quis nostrud exercitation ullamco laboris nisi ut aliquip ex ea commodo consequat.</p>
    <p>Excepteur sint occaecat cupidatat non proident, sunt in culpa qui officia deserunt mollit anim id est laborum. re et dolore magnam aliquam quaerat voluptatem.</p>
    <p class="closing">Regards</p>
    <div class="signature" role="img" aria-label="Handwritten signature of the sender"></div>
  </div>

  <div class="dealer">
    <span class="dealer-mark"></span>
    <span>Dorrit Falke Certified Dealer</span>
  </div>

  <div class="footer-address">410 SW Alder Row, Suite 120<br>Halden, OR 97015</div>
  <div class="footer-divider"></div>
  <div class="footer-contact">
    <span><svg viewBox="0 0 10 10"><path d="M2 1 L4 1 L4.6 3 L3.5 4 Q4.5 6 6 6.5 L7 5.4 L9 6 L9 8 Q5 9 2 5 Q1 3 2 1Z" fill="#fff"/></svg>541.660.2847</span>
    <span><svg viewBox="0 0 10 10"><rect x="1" y="2" width="8" height="6" fill="#fff"/><path d="M1 2 L5 5.5 L9 2" stroke="#557a6a" fill="none" stroke-width="0.8"/></svg>info@coralvexktn.com</span>
  </div>
  <div class="website">www.coralvexktn.com</div>
</section>

<section class="sheet envelope-front" aria-label="Envelope front">
  <svg class="bands" viewBox="0 0 500 217" aria-hidden="true">
    <polygon points="0,138 262,138 262,195 0,195" fill="var(--brand-green)"/>
    <polygon points="272,160 486,160 486,212 272,212" fill="var(--brand-grey)"/>
  </svg>
  <div class="brand">
    <span class="brand-mark"></span>
    <span class="brand-name">CoralvexKTN</span>
  </div>
  <div class="envelope-address">410 SW Alder Row, Suite 120, Halden, OR 97015</div>
  <div class="dealer">
    <span class="dealer-mark"></span>
    <span>Dorrit Falke Certified Dealer</span>
  </div>
  <div class="website">www.coralvexktn.com</div>
</section>

<section class="sheet envelope-back" aria-label="Envelope back">
  <svg class="bands" viewBox="0 0 500 217" aria-hidden="true">
    <path d="M8 0 H492 V50 Q492 66 476 66 H28 Q12 66 12 50 V0 Z" fill="var(--brand-green)"/>
  </svg>
</section>

</body>
</html>
```